Ostrel Appraisals BV business cards (a financial services company)

I am looking for a business card design that stands out in the financial advisory field of business & intellectual property valuation. The business card design should be conservative, yet different. Address details have changed since the attached business card. New address is:

Molenvlietkade 27
4817 KT Leiden
The Netherlands

Telephone number remains the same.

```html
<!DOCTYPE html>
<html lang="en">
<head>
<meta charset="utf-8">
<title>Ostrel Appraisals BV – Business Cards</title>
<link rel="stylesheet" href="https://fonts.googleapis.com/css2?family=Montserrat:wght@400;700&family=Roboto:wght@400&family=Roboto+Condensed:wght@400;700&display=swap">
<style>
  :root {
    --backdrop: #9a9a9a;
    --card-white: #ffffff;
    --ink: #6a6a6a;
    --ink-soft: #bdbdbd;
    --band: #6b6b6b;
    --band-text: #ffffff;
    --back-dark: #5f5f5f;
    --back-light: #8a8a8a;
  }
  * { margin: 0; padding: 0; box-sizing: border-box; }
  html, body { width: 1133px; height: 1200px; overflow: hidden; background: var(--backdrop); }
  .canvas { position: relative; width: 1133px; height: 1200px; }

  .card-front {
    position: absolute; left: 213px; top: 149px; width: 707px; height: 404px;
    background: var(--card-white); overflow: hidden;
  }
  .brand {
    position: absolute; right: 42px; top: 78px; width: 280px; text-align: center;
    color: var(--ink); font-family: "Montserrat", sans-serif;
  }
  .brand-name {
    display: flex; align-items: center; justify-content: center; gap: 10px;
    font-size: 25px; font-weight: 400; letter-spacing: 0.5px; line-height: 1;
  }
  .brand-mark { width: 14px; height: 14px; background: var(--ink); flex: none; }
  .brand-tagline {
    margin-top: 18px; font-size: 13.5px; font-weight: 700; line-height: 19px; letter-spacing: 0.2px;
  }

  .contact { position: absolute; left: 35px; top: 200px; color: var(--ink); font-family: "Roboto", sans-serif; }
  .person-name { font-family: "Roboto Condensed", sans-serif; font-weight: 700; font-size: 25px; line-height: 28px; }
  .person-creds { font-size: 17px; }
  .person-role { font-family: "Roboto", sans-serif; font-size: 16.5px; color: var(--ink-soft); line-height: 22px; }
  .address { margin-top: 14px; font-size: 16.5px; line-height: 22px; }
  .contact-line { display: flex; align-items: center; gap: 10px; font-size: 16.5px; line-height: 23px; }
  .contact-line:first-of-type { margin-top: 6px; }
  .contact-icon { width: 15px; height: 15px; fill: var(--ink); flex: none; }

  .footer-band { position: absolute; left: 0; bottom: 0; width: 707px; height: 26px; }
  .website {
    position: absolute; left: 38px; bottom: 4px; color: var(--band-text);
    font-family: "Roboto", sans-serif; font-size: 15px; letter-spacing: 5.2px;
  }

  .card-back {
    position: absolute; left: 216px; top: 647px; width: 698px; height: 399px;
    background: linear-gradient(100deg, var(--back-dark) 0%, var(--back-light) 50%, var(--back-dark) 100%);
  }
</style>
</head>
<body>
<div class="canvas">
  <section class="card-front">
    <div class="brand">
      <div class="brand-name"><span class="brand-mark"></span><span>OSTREL APPRAISALS</span></div>
      <p class="brand-tagline">BUSINESS AND INTELLECTUAL<br>PROPERTY VALUATIONS</p>
    </div>

    <div class="contact">
      <p class="person-name">Pieter Vandam, <span class="person-creds">CFA, ASA, RV</span></p>
      <p class="person-role">Managing Director</p>
      <p class="address">Molenvlietkade 27 , 4817<br>KT Leiden, The Netherlands</p>
      <p class="contact-line">
        <svg class="contact-icon" viewBox="0 0 24 24"><path d="M6.6 10.8a15.2 15.2 0 0 0 6.6 6.6l2.2-2.2a1 1 0 0 1 1-.25 11.4 11.4 0 0 0 3.6.57 1 1 0 0 1 1 1V20a1 1 0 0 1-1 1A17 17 0 0 1 3 4a1 1 0 0 1 1-1h3.5a1 1 0 0 1 1 1c0 1.25.2 2.45.57 3.57a1 1 0 0 1-.25 1z"/></svg>
        <span>+31(0)70 384 1962</span>
      </p>
      <p class="contact-line">
        <svg class="contact-icon" viewBox="0 0 24 24"><path d="M2 5h20v14H2z M3.5 6.5 12 12.5l8.5-6" fill="var(--ink)"/><path d="M3.5 7 12 12.8 20.5 7" stroke="#fff" stroke-width="1.6" fill="none"/></svg>
        <span>pvandam@ostrelappraisals.com</span>
      </p>
    </div>

    <svg class="footer-band" viewBox="0 0 707 26" aria-hidden="true">
      <polygon points="0,0 373,0 364,26 0,26" fill="var(--band)"/>
      <polygon points="372,0 366,26 369,26 375,0" fill="var(--band)"/>
      <rect x="380" y="0" width="327" height="2.5" fill="var(--band)"/>
      <rect x="378" y="8" width="329" height="2.5" fill="var(--band)"/>
      <rect x="375" y="16" width="332" height="2.5" fill="var(--band)"/>
    </svg>
    <p class="website">www.ostrelappraisals.com</p>
  </section>

  <section class="card-back" role="img" aria-label="Reverse of card: repeating embossed silver brand monogram pattern on grey"></section>
</div>
</body>
</html>
```